Innovative Fashion Business needs Branding and Business Card.

We need a Business Card and Branding work (Email Footer, Stickers, letterhead, all from same Design) We are an innovative, progressive and exciting Fashion Start-up. We are called "Moss Tide" I am attaching the original artwork of the image I want to use. Also have a previous Card, I want to do something like that, only using this new image.

```html
<!DOCTYPE html>
<html lang="en">
<head>
<meta charset="utf-8">
<title>Moss Tide — Business Card</title>
<link rel="stylesheet" href="https://fonts.googleapis.com/css2?family=Fauna+One&family=Quicksand:wght@600;700&display=swap">
<style>
  :root {
    --stage: #808080;
    --card: #f7f7f5;
    --purple: #6b3f8e;
    --ink: #4a4a4a;
    --art-light: #ecebf0;
    --art-mid: #c9bcd8;
    --art-deep: #8d6aad;
  }
  * { margin: 0; padding: 0; box-sizing: border-box; }
  html, body { width: 1200px; height: 459px; overflow: hidden; }
  body {
    position: relative;
    background: var(--stage);
    font-family: "Fauna One", Georgia, serif;
  }
  .card {
    position: absolute;
    top: 102px;
    width: 420px;
    height: 253px;
    background: var(--card);
    text-align: center;
  }
  .card--front { left: 158px; }
  .card--back { left: 622px; }

  .wordmark {
    position: absolute;
    top: 26px; left: 0; right: 0;
    font-family: "Quicksand", Arial, sans-serif;
    font-weight: 600;
    font-size: 31px;
    letter-spacing: 1px;
    line-height: 1;
    color: var(--purple);
    text-transform: uppercase;
  }
  .artwork {
    position: absolute;
    top: 60px; left: 107px;
    width: 206px; height: 156px;
  }
  .tagline {
    position: absolute;
    top: 225px; left: 0; right: 0;
    font-size: 11px;
    color: var(--ink);
  }

  .holder {
    position: absolute;
    top: 52px; left: 0; right: 0;
  }
  .holder__name {
    font-family: "Quicksand", Arial, sans-serif;
    font-weight: 700;
    font-size: 16px;
    color: var(--purple);
    line-height: 20px;
  }
  .holder__role {
    font-size: 10px;
    color: var(--ink);
    line-height: 15px;
  }
  .services {
    position: absolute;
    top: 106px; left: 0; right: 0;
    font-size: 11.5px;
    line-height: 15px;
    color: var(--ink);
  }
  .contact {
    position: absolute;
    top: 149px; left: 0; right: 0;
    list-style: none;
    font-size: 12.5px;
    line-height: 17px;
    color: var(--purple);
  }
</style>
</head>
<body>
  <section class="card card--front">
    <div class="wordmark">Moss Tide</div>
    <svg class="artwork" viewBox="0 0 206 156" role="img" aria-label="Line-art illustration in grey and purple: a couple with a cat, hearts, stars and a flower">
      <defs>
        <linearGradient id="art-tone" x1="0" y1="0" x2="0" y2="1">
          <stop offset="0" stop-color="var(--art-light)"/>
          <stop offset="0.7" stop-color="var(--art-mid)"/>
          <stop offset="1" stop-color="var(--art-deep)"/>
        </linearGradient>
      </defs>
      <rect width="206" height="156" fill="url(#art-tone)"/>
    </svg>
    <p class="tagline">Purveyors of Inspiration &amp; Opportunity</p>
  </section>

  <section class="card card--back">
    <div class="holder">
      <h1 class="holder__name">Hero Love</h1>
      <p class="holder__role">Partner &amp; Strategist</p>
    </div>
    <p class="services">Boutique development &amp; sourcing<br>Sustainbility &amp; innovation</p>
    <ul class="contact">
      <li>+852 5550 1846</li>
      <li>hero@mosstide.asia</li>
      <li>www.mosstide.asia</li>
    </ul>
  </section>
</body>
</html>
```